50 Lessons from my entrepreneurial journey

make a book cover (see attached file for reference or sample )
https://files.example-share.net/file/d/7kPqWz3rTn8LmYv2XcB5dHj9QsF0aUe4G/view?usp=share_link

make a back book cover (see writings below)

BUILD A BUSINESS. BUILD A LIFE.

What does it really take to succeed, not just in business, but in life?

In MARLO’S LEDGER, award-winning entrepreneur, speaker, and columnist Marlo Dantes shares 50 powerful lessons and more drawn from over three decades of building Cebu’s most beloved homegrown brands. Honest, practical, and deeply personal, this book brings together timeless insights on entrepreneurship, leadership, family, faith, and the inner journey of growth.

Whether you’re just starting out, scaling up, or searching for clarity in the next chapter of your life, these pages will guide, inspire, and challenge you to pursue something greater not just profit, but purpose. More than a business book, this is a book about building the kind of life you won’t need a vacation from.

About the Author

Marlo Dantes is one of Cebu’s most respected and successful entrepreneurs, best known for building iconic homegrown brands such as Breezy Coolers and Blends, Hall of Roastmeat, and The PEAK of Cebu. As Chairman and CEO of the Dantes Food Group, he has spent over 25 years shaping the business landscape of the Visayas and Mindanao. Named Entrepreneur of the Year by the Cebu Guild of Traders and Makers and recognized for one of the Top Ten Most Outstanding Family Businesses in the Philippines, Marlo is also a popular columnist for DayLamp Cebu. Through his writing and mentorship, he continues to empower the next generation to build with heart, lead with purpose, and live with meaning.

Target Market(s)

Millennials & Young Professionals

Industry/Entity Type

Entrepreneurship

Font styles to use
Serif
Sans Serif

Requirements
Must have
• Professional yet clean modern typography

```html
<!DOCTYPE html>
<html lang="en">
<head>
<meta charset="utf-8">
<title>50 Lessons from My Entrepreneurial Journey — Book Cover</title>
<link rel="stylesheet" href="https://fonts.googleapis.com/css2?family=Anton&family=Inter:wght@200;300;500&family=Montserrat:wght@300;400;500&display=swap">
<style>
  :root {
    --cover-blue: #164a96;
    --paper: #ffffff;
    --ink-light: #ffffff;
    --spine-ink: #164a96;
    --spine-author: #262a36;
    --barcode-border: #1a1a1a;
    --photo-warm: #c08d62;
    --photo-dark: #3a3634;
    --photo-denim: #5b82b8;
  }
  * { margin: 0; padding: 0; box-sizing: border-box; }
  html, body {
    width: 1200px; height: 1200px; overflow: hidden;
    background: var(--paper);
  }
  .canvas { position: relative; width: 1200px; height: 1200px; }
  .cover-spread {
    position: absolute; left: 66px; top: 219px;
    width: 1076px; height: 769px;
  }
  .panel { position: absolute; top: 0; height: 769px; }
  .back-cover { left: 0; width: 512px; background: var(--cover-blue); color: var(--ink-light); }
  .spine { left: 512px; width: 51px; background: var(--paper); }
  .front-cover { left: 563px; width: 513px; background: var(--cover-blue); }
  .panel svg { position: absolute; left: 0; top: 0; display: block; }

  .back-headline { font-family: "Anton", sans-serif; }
  .back-copy {
    position: absolute; left: 28px; width: 455px;
    font-family: "Montserrat", sans-serif;
  }
  .back-question { top: 72px; font-size: 19.5px; line-height: 25px; font-weight: 400; }
  .back-body {
    font-size: 11.9px; line-height: 19px; font-weight: 400;
    text-align: justify;
  }
  .back-body-first { top: 126.5px; }
  .back-body-second { top: 240px; }
  .author-block { top: 346px; }
  .author-photo {
    float: left; width: 109px; height: 129px;
    margin: 7px 11px 0 0; border-radius: 10px;
    background: linear-gradient(160deg, var(--photo-warm) 0%, #a87a55 55%, var(--photo-dark) 100%);
  }
  .author-name {
    font-family: "Montserrat", sans-serif; font-weight: 300;
    font-size: 26px; line-height: 28px; letter-spacing: 2.2px;
  }
  .author-bio {
    font-size: 11.9px; line-height: 19px; text-align: justify;
  }
  .barcode-area {
    position: absolute; left: 332px; top: 661px; width: 151px; height: 72px;
    background: var(--paper); border: 1px solid var(--barcode-border);
  }
  .title-bold { font-family: "Anton", sans-serif; }
  .title-light { font-family: "Inter", sans-serif; font-weight: 200; }
  .author-front { font-family: "Inter", sans-serif; font-weight: 500; }
</style>
</head>
<body>
<main class="canvas">
  <section class="cover-spread">

    <article class="panel back-cover">
      <svg width="512" height="90" viewBox="0 0 512 90" aria-label="Build a business. Build a life.">
        <text class="back-headline" x="28" y="63.5" font-size="36" fill="#ffffff" textLength="455" lengthAdjust="spacingAndGlyphs">BUILD A BUSINESS. BUILD A LIFE.</text>
      </svg>
      <p class="back-copy back-question">What does it really take to succeed, not just in business, but in life?</p>
      <p class="back-copy back-body back-body-first">In *MARLO’S LEDGER*, award-winning entrepreneur, speaker, and columnist Marlo Dantes shares 50 powerful lessons and more drawn from over three decades of building Cebu’s most beloved homegrown brands. Honest, practical, and deeply personal, this book brings together timeless insights on entrepreneurship, leadership, family, faith, and the inner journey of growth.</p>
      <p class="back-copy back-body back-body-second">Whether you’re just starting out, scaling up, or searching for clarity in the next chapter of your life, these pages will guide, inspire, and challenge you to pursue something greater not just profit, but purpose. More than a business book, this is a book about building the kind of life you won’t need a vacation from.</p>
      <div class="back-copy author-block">
        <div class="author-photo" role="img" aria-label="Portrait photo of the author smiling, wearing glasses and a dark blazer"></div>
        <h2 class="author-name">MARLO DANTES</h2>
        <p class="author-bio">Marlo Dantes is one of Cebu’s most respected and successful entrepreneurs, best known for building iconic homegrown brands such as Breezy Coolers and Blends, Hall of Roastmeat, and The PEAK of Cebu. As Chairman and CEO of the Dantes Food Group, he has spent over 25 years shaping the business landscape of the Visayas and Mindanao. Named Entrepreneur of the Year by the Cebu Guild of Traders and Makers and recognized for one of the Top Ten Most Outstanding Family Businesses in the Philippines, Marlo is also a popular columnist for DayLamp Cebu. Through his writing and mentorship, he continues to empower the next generation to build with heart, lead with purpose, and live with meaning.</p>
      </div>
      <div class="barcode-area" aria-hidden="true"></div>
    </article>

    <aside class="panel spine">
      <svg width="51" height="769" viewBox="0 0 51 769" aria-label="50 Lessons from My Entrepreneurial Journey, Marlo Dantes">
        <text class="title-bold" transform="translate(15 34) rotate(90)" font-size="29" fill="var(--spine-ink)" textLength="116" lengthAdjust="spacingAndGlyphs">50 LESSONS</text>
        <text class="title-light" transform="translate(16 156) rotate(90)" font-size="25" fill="var(--spine-ink)" textLength="80" lengthAdjust="spacingAndGlyphs">FROM MY</text>
        <text class="title-bold" transform="translate(15 243) rotate(90)" font-size="29" fill="var(--spine-ink)" textLength="166" lengthAdjust="spacingAndGlyphs">ENTREPRENEURIAL</text>
        <text class="title-light" transform="translate(16 415) rotate(90)" font-size="27" fill="var(--spine-ink)" textLength="123" lengthAdjust="spacingAndGlyphs">JOURNEY</text>
        <text class="title-light" transform="translate(17 584) rotate(90)" font-size="24" font-weight="300" fill="var(--spine-author)" textLength="150" lengthAdjust="spacingAndGlyphs">MARLO DANTES</text>
      </svg>
    </aside>

    <article class="panel front-cover">
      <svg width="513" height="769" viewBox="0 0 513 769" aria-label="50 Lessons from My Entrepreneurial Journey by Marlo Dantes">
        <defs>
          <linearGradient id="portrait-tones" x1="0" y1="0" x2="0" y2="1">
            <stop offset="0" stop-color="#b98a6a"/>
            <stop offset="0.18" stop-color="#4a4542"/>
            <stop offset="0.55" stop-color="#3c3a3a"/>
            <stop offset="0.75" stop-color="var(--photo-denim)"/>
            <stop offset="1" stop-color="#3f5f8f"/>
          </linearGradient>
        </defs>
        <rect x="95" y="268" width="307" height="501" rx="40" fill="url(#portrait-tones)" opacity="0.85" role="img" aria-label="Full-length photo of the author seated on a stool in a dark blazer and jeans, smiling"/>
        <text class="title-bold" x="32" y="113" font-size="104" fill="#ffffff" textLength="448" lengthAdjust="spacingAndGlyphs">50 LESSONS</text>
        <text class="title-light" x="163" y="158" font-size="50" fill="#ffffff" textLength="208" lengthAdjust="spacingAndGlyphs">FROM MY</text>
        <text class="title-bold" x="32" y="213" font-size="62" fill="#ffffff" textLength="448" lengthAdjust="spacingAndGlyphs">ENTREPRENEURIAL</text>
        <text class="title-light" x="95" y="275" font-size="71" fill="#ffffff" textLength="323" lengthAdjust="spacingAndGlyphs">JOURNEY</text>
        <text class="author-front" x="99" y="732" font-size="42" fill="#ffffff" textLength="315" lengthAdjust="spacingAndGlyphs">MARLO DANTES</text>
      </svg>
    </article>

  </section>
</main>
</body>
</html>
```